business card design for a small scale specialty cut flower farm

We need a business card design for Hollowmere Bloom Farm based in Langley, BC, Canada. We produce specialty, high-end cut flowers and sell locally to florists, local shops and markets and the end user through bouquet subscriptions. The final business card design should be memorable and have a timeless or vintage feel. We would prefer a square shape.
Updates

Target Market(s)

florists, shops and seasonal markets, local flower lovers

Industry/Entity Type

Floral

Contact Information for Business Card

Tamsin Ellery Voss, Grower
Langley, BC, Canada
website: hollowmerebloomfarm.example
instagram: @hollowmerebloomfarm
Tel: 555.317.4290
facebook: www.facebook.example/hollowmereblooms/

Font styles to use
Serif
Decorative
Script

Requirements
Must have
• soft black background colour on front side, the included logo and catch phrase: Fresh Local Seasonal
Nice to have
• phone number and website address on front of card, included photo 6539 incorporated onto the back, possibly photo 6609 as well.

```html
<!DOCTYPE html>
<html lang="en">
<head>
<meta charset="utf-8">
<title>Hollowmere Bloom Farm – Business Card</title>
<link rel="stylesheet" href="https://fonts.googleapis.com/css2?family=Arimo:wght@400;700&family=Great+Vibes&family=Lato:wght@300;400&display=swap">
<style>
  :root {
    --backdrop: #d6d6d6;
    --card: #231f20;
    --ink: #ffffff;
    --ink-soft: #e6e6e6;
    --bloom-pink: #e7a9c9;
    --bloom-leaf: #4f7f45;
  }
  * { margin: 0; padding: 0; box-sizing: border-box; }
  html, body { width: 1200px; height: 802px; overflow: hidden; }
  body {
    background: var(--backdrop);
    position: relative;
    color: var(--ink);
  }
  .card {
    position: absolute;
    top: 178px;
    width: 489px;
    height: 489px;
    background: var(--card);
  }
  .card--front { left: 94px; }
  .card--back { left: 624px; }
  .card__frame {
    position: absolute;
    inset: 17px;
    border: 2px solid var(--ink);
  }
  .line {
    position: absolute;
    left: 0;
    width: 100%;
    text-align: center;
    white-space: nowrap;
    line-height: 1.2;
  }
  .bloom-art {
    position: absolute;
    left: 150px;
    top: 76px;
    width: 190px;
    height: 140px;
    border-radius: 50%;
    background: radial-gradient(ellipse at 55% 50%, #e9e27a 0 10%, var(--bloom-pink) 28%, #c98aa9 55%, rgba(79,127,69,0.85) 80%, rgba(35,31,32,0) 100%);
  }
  .brand-name {
    font-family: "Lato", sans-serif;
    font-weight: 300;
    text-transform: uppercase;
  }
  .card--front .brand-name__primary { top: 236px; font-size: 48px; letter-spacing: 0.12em; }
  .card--front .brand-name__secondary { top: 318px; font-size: 34px; letter-spacing: 0.24em; }
  .tagline {
    font-family: "Great Vibes", cursive;
    font-size: 25px;
  }
  .card--front .tagline { top: 364px; }
  .established {
    font-family: "Lato", sans-serif;
    font-weight: 400;
    font-size: 13px;
    letter-spacing: 0.55em;
  }
  .card--front .established { top: 404px; }
  .catch-phrase {
    top: 428px;
    font-family: "Lato", sans-serif;
    font-weight: 300;
    font-size: 12px;
    letter-spacing: 0.3em;
    text-transform: uppercase;
    color: var(--ink-soft);
  }

  .card--back .brand-name__primary { top: 62px; font-size: 40px; letter-spacing: 0.12em; }
  .card--back .brand-name__secondary { top: 128px; font-size: 27px; letter-spacing: 0.24em; }
  .card--back .tagline { top: 162px; font-size: 20px; }
  .card--back .established { top: 196px; font-size: 11px; }

  .contact-name {
    top: 258px;
    font-family: "Arimo", sans-serif;
    font-weight: 700;
    font-size: 26px;
  }
  .contact-role {
    top: 292px;
    font-family: "Arimo", sans-serif;
    font-size: 17px;
  }
  .contact-location {
    top: 314px;
    font-family: "Arimo", sans-serif;
    font-size: 14px;
    color: var(--ink-soft);
  }
  .contact-detail {
    font-family: "Arimo", sans-serif;
    font-size: 15px;
  }
  .contact-detail--tel { top: 353px; }
  .contact-detail--web { top: 380px; }
  .contact-detail--insta { top: 407px; }
  .contact-detail--social { top: 433px; }
</style>
</head>
<body>
  <section class="card card--front">
    <div class="card__frame"></div>
    <div class="bloom-art" role="img" aria-label="Watercolour wild rose illustration with pink petals and green leaves"></div>
    <div class="line brand-name brand-name__primary">Hollowmere</div>
    <div class="line brand-name brand-name__secondary">Bloom Farm</div>
    <div class="line tagline">Specialty Cut Flowers</div>
    <div class="line established">EST.2019</div>
    <div class="line catch-phrase">Fresh Local Seasonal</div>
  </section>

  <section class="card card--back">
    <div class="card__frame"></div>
    <div class="line brand-name brand-name__primary">Hollowmere</div>
    <div class="line brand-name brand-name__secondary">Bloom Farm</div>
    <div class="line tagline">Specialty Cut Flowers</div>
    <div class="line established">EST.2019</div>
    <div class="line contact-name">Tamsin Ellery Voss</div>
    <div class="line contact-role">Grower</div>
    <div class="line contact-location">Langley, BC, Canada</div>
    <div class="line contact-detail contact-detail--tel">Tel: (555) 317-4290</div>
    <div class="line contact-detail contact-detail--web">website: hollowmerebloomfarm.example</div>
    <div class="line contact-detail contact-detail--insta">instagram: @hollowmerebloomfarm</div>
    <div class="line contact-detail contact-detail--social">facebook: www.facebook.example/hollowmereblooms</div>
  </section>
</body>
</html>
```